Personal Finance e-commerce website needs a simple budget design

Hello! I am starting to sell downloadable and printable budget planners, as shown in the attached file, for people to plan ahead on their personal finances. <br/><br/>I want to see a one-page design with similar columns (for example, "Expenses, Budget, and Actual"). I would also like to see the basic formula ("Net Income = Gross income - Total Expenses") somewhere on the design. Finally, I want the design to remain mostly minimalistic and simple for the average person to plan their personal monthly budgets.<br/><br/>However, other than that, the overall design, layout, and colors will be at the graphic designer's choice. If you have any questions for me, please let me know. Thank you for your time!

Industry/Entity Type

Financial Planning

Colors

Designer to choose colors to be used in the design.

Requirements
Must have
• I want to see a one-page design with similar columns (for example, "Expenses, Budget, and Actual").
• I want the design to remain mostly minimalistic and simple for the average person to plan their personal monthly budgets.
Nice to have
• I would also like to see the basic formula ("Net Income = Gross income - Total Expenses") somewhere on the design.

```html
<!DOCTYPE html>
<html lang="en">
<head>
<meta charset="utf-8">
<title>Basic Monthly Budget</title>
<link href="https://fonts.googleapis.com/css2?family=Open+Sans:ital,wght@0,400;0,600;1,400&display=swap" rel="stylesheet">
<style>
  :root {
    --ink: #111111;
    --ink-soft: #333333;
    --muted: #777777;
    --hint: #a6a6a6;
    --row-shade: #f1f1f1;
    --col-shade: #f4f4f4;
    --cross-shade: #e7e7e7;
    --red: #c8001e;
    --green: #44ff11;
    --dark: #333333;
    --net: #44ff44;
    --gross: #22cc00;
    --total: #ff1a2a;
    --operator: #555555;
  }
  * { box-sizing: border-box; margin: 0; padding: 0; }
  html, body { width: 849px; height: 1200px; overflow: hidden; background: #ffffff; }
  body { font-family: "Open Sans", sans-serif; color: var(--ink); position: relative; }

  .promo { position: absolute; top: 19px; left: 0; width: 849px; text-align: center; font-size: 16px; color: var(--muted); }
  .promo .site { border-bottom: 1px dashed var(--muted); }

  .brand { position: absolute; left: 77px; top: 118px; font-weight: 600; font-size: 26px; line-height: 34px; color: var(--ink-soft); }

  .doc-title { position: absolute; right: 77px; top: 97px; font-size: 16px; letter-spacing: 1.4px; color: var(--ink-soft); }
  .date-line { position: absolute; top: 142px; height: 1.5px; background: var(--ink-soft); }
  .date-line.month { left: 666px; width: 36px; }
  .date-line.year { left: 719px; width: 53px; }
  .date-hint { position: absolute; right: 77px; top: 144px; font-size: 17px; letter-spacing: 1.8px; color: var(--hint); }

  .budget-col { position: absolute; left: 354px; top: 214px; width: 209px; height: 799px; background: var(--col-shade); }

  .col-head { position: absolute; top: 224px; }
  .col-head h2 { font-size: 20.5px; font-weight: 600; color: var(--ink); line-height: 30px; }
  .col-head p { font-size: 16px; color: var(--muted); line-height: 26px; }
  .col-head.expenses { left: 77px; }
  .col-head.budget { left: 370px; }
  .col-head.actual { left: 579px; }

  .rule { position: absolute; top: 288px; height: 5px; }
  .rule.expenses { left: 77px; width: 277px; background: var(--red); }
  .rule.budget { left: 354px; width: 209px; background: var(--green); }
  .rule.actual { left: 563px; width: 209px; background: var(--dark); }

  .rows { position: absolute; left: 77px; top: 293px; width: 695px; }
  .row { height: 60px; display: flex; }
  .row .cell { height: 60px; }
  .row .cell.expense { width: 277px; }
  .row .cell.budget { width: 209px; }
  .row .cell.actual { width: 209px; }
  .row.shaded .cell.expense, .row.shaded .cell.actual { background: var(--row-shade); }
  .row.shaded .cell.budget { background: var(--cross-shade); }

  .formula { position: absolute; top: 1061px; left: 0; width: 849px; height: 80px; }
  .term { position: absolute; top: 0; text-align: center; }
  .term .label { height: 37px; line-height: 37px; color: #ffffff; font-size: 20.5px; }
  .term .note { margin-top: 4px; font-style: italic; font-size: 15.5px; line-height: 17px; color: var(--ink-soft); }
  .term.net { left: 107px; width: 163px; }
  .term.net .label { background: var(--net); }
  .term.gross { left: 342px; width: 180px; }
  .term.gross .label { background: var(--gross); }
  .term.total { left: 569px; width: 173px; }
  .term.total .label { background: var(--total); }
  .operator { position: absolute; top: 0; }
  .operator.equals { left: 293px; }
  .operator.minus { left: 538px; }
</style>
</head>
<body>
  <p class="promo">Visit us at <span class="site">danawhitlow.com</span> for personal financial advice!</p>

  <p class="brand">Dana Whitlow</p>

  <p class="doc-title">BASIC MONTHLY BUDGET</p>
  <div class="date-line month"></div>
  <div class="date-line year"></div>
  <p class="date-hint">MM / YYYY</p>

  <div class="budget-col"></div>

  <div class="col-head expenses"><h2>Expenses (Category)</h2><p>Custom Category</p></div>
  <div class="col-head budget"><h2>Budget (USD)</h2><p>What you plan to spend</p></div>
  <div class="col-head actual"><h2>Actual (USD)</h2><p>What you actually spent</p></div>

  <div class="rule expenses"></div>
  <div class="rule budget"></div>
  <div class="rule actual"></div>

  <div class="rows">
    <div class="row"><div class="cell expense"></div><div class="cell budget"></div><div class="cell actual"></div></div>
    <div class="row shaded"><div class="cell expense"></div><div class="cell budget"></div><div class="cell actual"></div></div>
    <div class="row"><div class="cell expense"></div><div class="cell budget"></div><div class="cell actual"></div></div>
    <div class="row shaded"><div class="cell expense"></div><div class="cell budget"></div><div class="cell actual"></div></div>
    <div class="row"><div class="cell expense"></div><div class="cell budget"></div><div class="cell actual"></div></div>
    <div class="row shaded"><div class="cell expense"></div><div class="cell budget"></div><div class="cell actual"></div></div>
    <div class="row"><div class="cell expense"></div><div class="cell budget"></div><div class="cell actual"></div></div>
    <div class="row shaded"><div class="cell expense"></div><div class="cell budget"></div><div class="cell actual"></div></div>
    <div class="row"><div class="cell expense"></div><div class="cell budget"></div><div class="cell actual"></div></div>
    <div class="row shaded"><div class="cell expense"></div><div class="cell budget"></div><div class="cell actual"></div></div>
    <div class="row"><div class="cell expense"></div><div class="cell budget"></div><div class="cell actual"></div></div>
    <div class="row shaded"><div class="cell expense"></div><div class="cell budget"></div><div class="cell actual"></div></div>
  </div>

  <div class="formula">
    <div class="term net"><div class="label">Net income</div><p class="note">How much money<br>you kept.</p></div>
    <svg class="operator equals" width="25" height="37" viewBox="0 0 25 37" aria-hidden="true">
      <rect x="0" y="13" width="25" height="4" fill="#555555"/>
      <rect x="0" y="21" width="25" height="4" fill="#555555"/>
    </svg>
    <div class="term gross"><div class="label">Gross income</div><p class="note">How much money<br>you earned.</p></div>
    <svg class="operator minus" width="15" height="37" viewBox="0 0 15 37" aria-hidden="true">
      <rect x="0" y="17" width="15" height="4" fill="#555555"/>
    </svg>
    <div class="term total"><div class="label">Total Expenses</div><p class="note">Actual expenses.</p></div>
  </div>
</body>
</html>
```